RM Skyline Imaging Web Site design

I am looking for a responsive single page website deign for rmskylineimages.com. This is a drone based aerial photography and cinematography business. It should have an about us section, a services section that contains photograph service, Video footage, and Aerial mapping all under the services section, a pricing section, and then a contact page for customers to contact us.

Coding

Coded - Design and coding required

Number of Pages Required

1 page

Font styles to use
Sans Serif

Colors

Designer to choose colors to be used in the design.

Requirements
Must have
• Responsive design. About us section, services section, pricing section under the services links, and contact us section, that links to a submission page where they can send Name, address, email, and comments on what they are interested in.
• See hoverlens7.com - looking for similar design.
Should not have
• clutter, or too busy design

```html
<!DOCTYPE html>
<html lang="en">
<head>
<meta charset="utf-8">
<title>RM Skyline Imaging — Aerial Photography</title>
<link href="https://fonts.googleapis.com/css2?family=Open+Sans:wght@400;600;700&family=Raleway:wght@500;600;700&display=swap" rel="stylesheet">
<style>
:root{
  --orange:#f39a1e;
  --ink:#222;
  --grey-text:#777;
  --light:#eeeeee;
  --white:#fff;
  --black:#0b0b0b;
  --sky-a:#6f8fa8;
  --sky-b:#c9d4dc;
}
*{box-sizing:border-box;margin:0;padding:0}
html,body{width:1200px;height:3772px;overflow:hidden}
body{position:relative;background:var(--white);font-family:"Open Sans",Arial,sans-serif;color:var(--ink)}
.abs{position:absolute}
.brand{display:flex;align-items:center;gap:10px;font-family:"Raleway",Arial,sans-serif;font-weight:600;font-size:18px;color:var(--ink);letter-spacing:1px}
.brand .dot{width:14px;height:14px;border-radius:50%;background:var(--orange)}
/* header */
.site-header{left:0;top:0;width:1200px;height:88px;background:var(--white);display:flex;align-items:center;justify-content:space-between;padding:0 96px}
.main-nav{display:flex;gap:40px;font-size:15px}
.main-nav a{color:var(--ink);text-decoration:none}
/* hero */
.hero{left:0;top:88px;width:1200px;height:612px;background:linear-gradient(180deg,#4f7896 0%,#8fa9bd 45%,#d8dfe4 70%,#5b5f63 100%)}
.hero-title{left:64px;top:350px;font-family:"Raleway",Arial,sans-serif;font-weight:700;font-size:56px;line-height:60px;color:var(--white);letter-spacing:2px}
.hero-title em{font-style:normal;color:var(--orange)}
.accent-line{width:4px;height:100px;background:var(--orange);left:178px}
.section-title{font-family:"Raleway",Arial,sans-serif;font-weight:600;font-size:54px;letter-spacing:1px;color:var(--ink);left:64px}
/* services */
.service{width:300px;text-align:center}
.service .photo{width:220px;height:220px;border-radius:50%;margin:0 auto;border:4px solid #ddd}
.service h3{margin-top:34px;font-family:"Raleway",Arial,sans-serif;font-size:17px;font-weight:700;color:#555;letter-spacing:1px}
.blurb{font-size:14px;line-height:22px;color:var(--grey-text);margin-top:12px}
/* about */
.about{left:0;top:1360px;width:1200px;height:560px;background:var(--light)}
.about-inner{width:1200px;text-align:center}
.about h4{font-family:"Raleway",Arial,sans-serif;font-size:20px;font-weight:700;color:#444;letter-spacing:1px}
.about p{width:1000px;margin:22px auto 0;font-size:17px;line-height:28px;color:var(--grey-text)}
.btn{display:inline-block;background:var(--orange);color:var(--white);font-weight:700;font-size:15px;padding:10px 28px;letter-spacing:1px}
.call{font-family:"Raleway",Arial,sans-serif;font-size:22px;font-weight:700;color:#444}
.call span{color:var(--orange)}
/* pricing */
.price-card{background:var(--orange);color:var(--white);text-align:center;padding-top:58px}
.price-card h5{font-size:18px;font-weight:700;letter-spacing:1px}
.price-card b{display:block;font-size:22px;margin-top:8px}
.price-card p{width:280px;margin:12px auto 0;font-size:14px;line-height:20px}
.tile{}
/* pilots */
.pilots{left:0;top:2640px;width:1200px;height:540px;background:var(--light)}
.pilot{width:240px;text-align:center}
.pilot .photo{width:188px;height:188px;border-radius:50%;margin:0 auto;border:5px solid #fff;box-shadow:0 0 0 2px #ccc;background:linear-gradient(160deg,#b7c2c8,#55606a)}
.pilot h3{margin-top:30px;font-family:"Raleway",Arial,sans-serif;font-size:17px;font-weight:700;color:#555;letter-spacing:1px}
/* contact */
.contact{left:0;top:3180px;width:1200px;height:592px;background:var(--black);color:var(--white)}
.contact .section-title{color:var(--white)}
.field{left:64px;width:296px;height:30px;background:var(--white);color:#999;font-size:11px;padding:8px 10px}
.submit{left:64px;top:420px;width:120px;height:36px;background:var(--orange);color:var(--white);font-weight:700;font-size:14px;text-align:center;line-height:36px;letter-spacing:1px}
.footer-col{font-size:13px;line-height:24px;color:#ddd}
.footer-col h6{font-size:14px;font-weight:700;color:var(--white);margin-bottom:8px;letter-spacing:1px}
.footer-col li{list-style:none;display:flex;align-items:center;gap:10px}
.footer-col li::before{content:"";width:6px;height:6px;border-radius:50%;background:var(--white)}
.icon-row{display:flex;align-items:center;gap:12px}
.legal{left:440px;top:440px;width:690px;font-size:13px;line-height:21px;color:#ccc}
</style>
</head>
<body>

<header class="abs site-header">
  <div class="brand"><span class="dot"></span>RM Skyline Imaging</div>
  <nav class="main-nav"><a>Home</a><a>About Us</a><a>Services</a><a>Video Footage</a><a>Pricing</a><a>Contacts</a></nav>
</header>

<section class="abs hero" role="img" aria-label="Photo of a man flying a camera drone above a sea of clouds"></section>
<h1 class="abs hero-title">FROM A <em>DIFFERENT</em><br>POINT OF VIEW</h1>

<div class="abs accent-line" style="top:720px"></div>
<h2 class="abs section-title" style="top:830px">SERVICES</h2>

<div class="abs service" style="left:132px;top:940px">
  <div class="photo" role="img" aria-label="Close-up photo of a camera lens" style="background:radial-gradient(circle,#1a1a1a 30%,#6b5a4a 60%,#d9c7a8)"></div>
  <h3>PHOTOGRAPH SERVICE</h3>
  <p class="blurb">I'm a paragraph. Click here to add your own text and edit me. Let your users get to know you.</p>
</div>
<div class="abs service" style="left:460px;top:940px">
  <div class="photo" role="img" aria-label="Photo of a drone hovering over a wedding couple" style="background:linear-gradient(180deg,#6ea3d8,#a9cfe8 60%,#8fae6a)"></div>
  <h3>VIDEO FOOTAGE</h3>
  <p class="blurb">I'm a paragraph. Click here to add your own text and edit me. Let your users get to know you.</p>
</div>
<div class="abs service" style="left:788px;top:940px">
  <div class="photo" role="img" aria-label="Aerial photo of a park with drone overlay" style="border-radius:0;border:none;background:linear-gradient(135deg,#7d9a6a,#b8c3a6 50%,#6b8560)"></div>
  <h3>AERIAL MAPPING</h3>
  <p class="blurb">I'm a paragraph. Click here to add your own text and edit me. Let your users get to know you.</p>
</div>

<section class="abs about">
  <div class="abs accent-line" style="top:0;height:70px"></div>
  <h2 class="abs section-title" style="top:88px">ABOUT US</h2>
  <div class="abs about-inner" style="top:176px">
    <div class="brand" style="justify-content:center"><span class="dot"></span>RM Skyline Imaging</div>
    <h4 style="margin-top:40px">NEW PHOTOGRAPHY OPPORTUNITIES USING DRONES</h4>
    <p>I'm a paragraph. Click here to add your own text and edit me. It's easy. Just click "Edit Text" or double click me to add your own content and make changes to the font. Feel free to drag and drop me anywhere you like on your page. I'm a great place for you to tell a story and let your users know a little more about you.</p>
    <div style="margin-top:26px"><span class="btn">READ MORE</span></div>
    <p class="call" style="margin-top:26px;width:auto">
      CALL US
      <svg width="20" height="20" viewBox="0 0 24 24" style="vertical-align:-3px"><path fill="#f39a1e" d="M6.6 10.8a15 15 0 0 0 6.6 6.6l2.2-2.2a1 1 0 0 1 1-.3 11.4 11.4 0 0 0 3.6.6 1 1 0 0 1 1 1V20a1 1 0 0 1-1 1A17 17 0 0 1 3 4a1 1 0 0 1 1-1h3.5a1 1 0 0 1 1 1 11.4 11.4 0 0 0 .6 3.6 1 1 0 0 1-.3 1z"/></svg>
      <span>555-210-4478</span>
    </p>
  </div>
</section>

<div class="abs accent-line" style="top:1920px;height:110px"></div>
<h2 class="abs section-title" style="top:2000px">OUR PRICING</h2>

<div class="abs price-card" style="left:64px;top:2100px;width:388px;height:220px">
  <h5>AVERAGE</h5>
  <b>$400 TO $1500</b>
  <p>I'm a paragraph. Click here to add your own text and edit me. Let your users get to know you.</p>
</div>
<div class="abs tile" role="img" aria-label="Aerial photo of a golf course" style="left:472px;top:2100px;width:248px;height:460px;background:linear-gradient(160deg,#5f7f3e,#9db46a 50%,#4f6b36)"></div>
<div class="abs tile" role="img" aria-label="Photo of a helicopter on a landing pad" style="left:744px;top:2100px;width:388px;height:220px;background:linear-gradient(180deg,#8fb4d8,#cfdde8 60%,#8a8f90)"></div>
<div class="abs tile" role="img" aria-label="Aerial photo of a city street" style="left:64px;top:2340px;width:388px;height:220px;background:linear-gradient(135deg,#8b7560,#c4b6a2 50%,#6d7b6a)"></div>
<div class="abs tile" role="img" aria-label="Aerial photo of beachfront homes" style="left:744px;top:2340px;width:388px;height:220px;background:linear-gradient(180deg,#c9c2b5,#9fb0b8 55%,#4f7f9a)"></div>

<section class="abs pilots">
  <div class="abs accent-line" style="top:0;height:70px"></div>
  <h2 class="abs section-title" style="top:56px">DRONE PILOTS</h2>
  <div class="abs pilot" style="left:60px;top:172px"><div class="photo" role="img" aria-label="Portrait photo of a drone pilot"></div><h3>PILOT: JHON DOE</h3><p class="blurb">I'm a paragraph. Click here to add your own text and edit me. Let your users get to know you.</p></div>
  <div class="abs pilot" style="left:340px;top:172px"><div class="photo" role="img" aria-label="Portrait photo of a drone pilot"></div><h3>PILOT: JHON DOE</h3><p class="blurb">I'm a paragraph. Click here to add your own text and edit me. Let your users get to know you.</p></div>
  <div class="abs pilot" style="left:620px;top:172px"><div class="photo" role="img" aria-label="Portrait photo of a drone pilot"></div><h3>PILOT: JHON DOE</h3><p class="blurb">I'm a paragraph. Click here to add your own text and edit me. Let your users get to know you.</p></div>
  <div class="abs pilot" style="left:900px;top:172px"><div class="photo" role="img" aria-label="Portrait photo of a drone pilot"></div><h3>PILOT: JHON DOE</h3><p class="blurb">I'm a paragraph. Click here to add your own text and edit me. Let your users get to know you.</p></div>
</section>

<section class="abs contact">
  <div class="abs accent-line" style="top:0;height:80px"></div>
  <h2 class="abs section-title" style="top:92px">CONTACT US</h2>
  <div class="abs field" style="top:196px">Name</div>
  <div class="abs field" style="top:236px">Address</div>
  <div class="abs field" style="top:276px">Email</div>
  <div class="abs field" style="top:316px;height:80px">Comments</div>
  <div class="abs submit">SUBMIT</div>

  <div class="abs brand" style="left:880px;top:40px;color:var(--white)"><span class="dot"></span>RM Skyline Imaging</div>

  <div class="abs footer-col" style="left:440px;top:140px;width:250px">
    <h6>PHOTOGRAPHS BY RM SKYLINE IMAGING</h6>
    <p style="font-weight:700;color:#fff">ADDRESS</p>
    <div class="icon-row"><svg width="14" height="18" viewBox="0 0 24 30"><path fill="#fff" d="M12 0a10 10 0 0 0-10 10c0 7 10 20 10 20s10-13 10-20A10 10 0 0 0 12 0zm0 14a4 4 0 1 1 0-8 4 4 0 0 1 0 8z"/></svg><span>214 Harbor Crest Lane<br>Bayview, CA 90000</span></div>
    <div class="icon-row"><svg width="14" height="14" viewBox="0 0 24 24"><rect x="2" y="5" width="20" height="14" fill="none" stroke="#fff" stroke-width="2"/><path d="M2 5l10 8 10-8" fill="none" stroke="#fff" stroke-width="2"/></svg>hello@rmskylineimages.com</div>
    <div class="icon-row"><svg width="14" height="14" viewBox="0 0 24 24"><path fill="#fff" d="M6.6 10.8a15 15 0 0 0 6.6 6.6l2.2-2.2a1 1 0 0 1 1-.3 11.4 11.4 0 0 0 3.6.6 1 1 0 0 1 1 1V20a1 1 0 0 1-1 1A17 17 0 0 1 3 4a1 1 0 0 1 1-1h3.5a1 1 0 0 1 1 1 11.4 11.4 0 0 0 .6 3.6 1 1 0 0 1-.3 1z"/></svg>555-210-4478</div>
    <div class="icon-row"><svg width="14" height="14" viewBox="0 0 24 24"><circle cx="12" cy="12" r="10" fill="none" stroke="#fff" stroke-width="2"/></svg>rmskylineimages.com</div>
  </div>

  <div class="abs footer-col" style="left:730px;top:170px">
    <h6>LINKS:</h6>
    <ul><li>Home</li><li>About Us</li><li>Services</li><li>Video Footage</li><li>Pricing</li><li>Contacts</li></ul>
  </div>

  <div class="abs footer-col" style="left:900px;top:170px">
    <h6>SERVICES</h6>
    <ul><li>Camera Photograph Service</li><li>Video Footage</li><li>Aerial mapping</li></ul>
  </div>

  <p class="abs legal">RM Skyline Imaging provides services for Real Estate, Architectural, Sports, Commercial Advertising, Environmental, professionals or personal aerial photo sessions. We serve the coastal and inland valley regions with the best aerial photography around. All photographs are copyright protected and the property of RM Skyline Imaging.</p>
</section>

</body>
</html>
```